Site Design - PSD Only - festival management

We are looking for a final design for our B2B marketplace. The project is a social commerce platform managing the application and transaction process for festivals and local events. The site design should be based on either Bootstrap or Zurb Foundation. We will provide logos and example images.

Two of the most critical pages will be the home page and the search interface, as well several dashboards. Beyond that, most of the pages will be standard forms and other typical pages that drop into the general site theme. The design tends towards minimalism to simplify the UX and speed up the interface. It incorporates elements from the the following websites. Although the wireframes may lift design elements directly from some of these sites, we are looking for a design that incorporates them more as inspiration.

brivel.co - good example of minimalist structure on internal pages
tovemix.com - some similarities on search pages, etc.
quenlar.com - nice simple layout for features on home and internal pages
mossbarrels.com - nice alternative to standard bootstrap template
Updates

We're nearing the end of this project.  I've received some good submissions , but they are all variations on the exact same theme.  I would still like to see something that doesn't look like a bootstrap template.  I suggested the following idea to a few of the submitters, but now I am adding it to the main project description in hopes of stoking the engine.

The idea I had is for something a little less "bootstrappy" riffs on the design at mossbarrels.com with a flat background color that nicely offsets the blue in the logo. Rather than pulling in a stock image I thought about creating a derivation of the iconic Harrowmere poster, perhaps with vendor tents as tuning pegs and a silhouette of people on the neck. Just throwing that out there. 

I'm not a designer, though, so here's hoping we can see some different ideas while the project is still open.

Thanks.

Target Market(s)

Target market: Festival and event organizers; event participants including exhibitors, vendors, musicians, authors, volunteers, etc.

Industry/Entity Type

Festival

Requirements
Must have
• Home page, Search page, User dash, Organization dash, Event dash, Features, FAQ, various forms
Nice to have
• Would like to see some alternative designs to the standard bootstrap templates...creativity is encouraged.
Should not have
• Should not look like it was pulled off of the shelf.

```html
<!DOCTYPE html>
<html lang="en">
<head>
<meta charset="utf-8">
<title>Corvana — Festival & Event Network</title>
<link href="https://fonts.googleapis.com/css2?family=Exo+2:wght@400;500;600;800;900&family=Arimo:wght@400&display=swap" rel="stylesheet">
<style>
:root{
  --brand-blue:#2a7fc6;
  --link-blue:#2b86cc;
  --ink:#2b2b2b;
  --muted:#555;
  --band:#3f4042;
  --pink:#e4107a;
  --footer:#494a4b;
  --line:#d4d4d4;
  --white:#fff;
}
*{box-sizing:border-box;margin:0;padding:0}
html,body{width:955px;height:1200px;overflow:hidden;background:var(--white)}
body{position:relative;font-family:"Exo 2",sans-serif;color:var(--ink)}

/* header */
.site-header{position:absolute;left:0;top:0;width:955px;height:102px;background:var(--white)}
.brand{position:absolute;left:16px;top:30px;display:flex;align-items:center;gap:6px}
.brand-mark{width:16px;height:16px;border-radius:50%;background:var(--brand-blue)}
.brand-name{font-size:17px;font-weight:600;color:var(--brand-blue)}
.callout{position:absolute;top:0;height:102px;border-left:1px solid var(--line);padding:22px 0 0 12px;width:105px}
.callout-last{border-right:1px solid var(--line)}
.callout h3{font-size:15px;font-weight:600;color:var(--brand-blue);line-height:16px}
.callout p{font-size:12px;color:var(--muted);line-height:13.5px;width:82px}
.search{position:absolute;left:705px;top:26px;width:174px;height:24px;border:1px solid #999;border-radius:5px}
.search svg{position:absolute;right:5px;top:4px}
.social-top{position:absolute;top:28px;width:19px;height:19px;border-radius:3px}
.main-nav{position:absolute;left:0;top:66px;width:955px;font-size:10.5px;font-weight:600}
.main-nav a{position:absolute;color:var(--ink);text-decoration:none}

/* hero */
.hero{position:absolute;left:0;top:102px;width:955px;height:370px;
  background:linear-gradient(180deg,#4d5f86 0%,#3e4f7c 35%,#26305a 65%,#0d1022 100%)}
.hero-title{position:absolute;left:54px;top:74px;width:410px;height:58px;background:rgba(40,44,60,.78);
  color:var(--white);font-weight:900;font-size:47px;line-height:58px;padding-left:12px;letter-spacing:-1px}
.hero-sub{position:absolute;left:54px;top:133px;width:459px;height:58px;background:rgba(235,238,245,.9);
  font-size:15px;line-height:18px;padding:10px 12px;color:#333}
.hero-cta{position:absolute;left:54px;top:223px;width:148px;height:30px;background:var(--pink);color:var(--white);
  font-size:13px;font-weight:600;text-align:center;line-height:30px}

/* features */
.feature{position:absolute;width:224px;height:260px;background:var(--white);border:1px solid #ddd;box-shadow:0 1px 3px rgba(0,0,0,.25)}
.feature-icon{position:absolute;left:78px;top:16px;width:68px;height:68px;border-radius:10px}
.feature-band{position:absolute;left:0;top:99px;width:100%;height:58px;background:var(--band);color:var(--white);
  display:flex;align-items:center;justify-content:center;text-align:center;font-size:14.5px;font-weight:400;line-height:17.5px;padding:0 16px;letter-spacing:.3px}
.feature-text{position:absolute;left:14px;top:171px;width:194px;text-align:center;font-family:"Arimo",sans-serif;font-size:10.5px;line-height:14.5px;color:#777}
.feature-btn{position:absolute;left:67px;top:227px;width:89px;height:20px;background:var(--link-blue);color:var(--white);
  font-size:9px;font-weight:600;text-align:center;line-height:20px}

/* footer */
.site-footer{position:absolute;left:0;top:1065px;width:955px;height:135px;background:var(--footer);color:var(--white)}
.footer-nav{position:absolute;left:0;top:38px;font-size:10.5px;font-weight:600}
.footer-nav span{position:absolute;white-space:nowrap}
.contact{position:absolute;top:64px;font-family:"Arimo",sans-serif;font-size:10px;display:flex;align-items:center;gap:6px;white-space:nowrap}
.copyright{position:absolute;left:122px;top:92px;font-family:"Arimo",sans-serif;font-size:10px}
.newsletter-title{position:absolute;left:575px;top:27px;font-size:18px;font-weight:500}
.newsletter-input{position:absolute;left:573px;top:60px;width:210px;height:22px;background:var(--white);color:#333;
  font-family:"Arimo",sans-serif;font-size:10px;line-height:22px;padding-left:8px}
.newsletter-send{position:absolute;left:789px;top:60px;width:60px;height:22px;background:var(--pink);font-size:13px;font-weight:600;text-align:center;line-height:22px}
.follow{position:absolute;left:573px;top:101px;font-size:13px;font-weight:600;white-space:nowrap}
.social-foot{position:absolute;top:100px;width:19px;height:19px;border-radius:3px;background:#6f7071}
</style>
</head>
<body>

<header class="site-header">
  <div class="brand"><span class="brand-mark"></span><span class="brand-name">Corvana</span></div>
  <div class="callout" style="left:120px"><h3>APPLY...</h3><p>to a fastival or local event</p></div>
  <div class="callout" style="left:225px"><h3>ADD...</h3><p>your event to the Corvana network</p></div>
  <div class="callout callout-last" style="left:330px"><h3>JOIN...</h3><p>discussions with industry professionals</p></div>
  <div class="search">
    <svg width="16" height="16" viewBox="0 0 16 16"><circle cx="6.5" cy="6.5" r="5" fill="none" stroke="#222" stroke-width="1.6"/><line x1="10" y1="10" x2="15" y2="15" stroke="#222" stroke-width="2"/></svg>
  </div>
  <span class="social-top" style="left:888px;background:#3b5b9a"></span>
  <span class="social-top" style="left:914px;background:#4bb4e0"></span>
  <nav class="main-nav">
    <a style="left:549px">ABOUT</a><a style="left:605px">FEATURES</a><a style="left:678px">FAQ</a>
    <a style="left:724px">BLOG</a><a style="left:779px">PRESS</a><a style="left:836px">REGISTER</a><a style="left:903px">LOGIN</a>
  </nav>
</header>

<section class="hero" role="img" aria-label="Concert crowd with raised hands under stage lights in a festival hall">
  <h1 class="hero-title">PEACE OF MIND</h1>
  <p class="hero-sub">Welcome to Corvana. We connect festival and event organizers with the people that make it happen.</p>
  <div class="hero-cta">GET STARTED</div>
</section>

<main>
  <article class="feature" style="left:104px;top:495px">
    <div class="feature-icon" role="img" aria-label="Server drive icon" style="background:linear-gradient(#eceef0,#9aa0a6)"></div>
    <h2 class="feature-band">ONLINE APPLICATIONS</h2>
    <p class="feature-text">This is a simple hero unit, a simple jumbotron- style component for calling extra attention to featured content.</p>
    <div class="feature-btn">LEARN MORE</div>
  </article>
  <article class="feature" style="left:365px;top:495px">
    <div class="feature-icon" role="img" aria-label="Calendar icon" style="background:linear-gradient(#2f8fd8 0 25%,#f2f2f2 25%);border:3px solid #333"></div>
    <h2 class="feature-band">INTEGRATED SCHEDULING</h2>
    <p class="feature-text">This is a simple hero unit, a simple jumbotron- style component for calling extra attention to featured content.</p>
    <div class="feature-btn">LEARN MORE</div>
  </article>
  <article class="feature" style="left:626px;top:495px">
    <div class="feature-icon" role="img" aria-label="Mobile app icon" style="background:linear-gradient(#b9dc3c,#6ea617)"></div>
    <h2 class="feature-band">NATIVE PHONE AND TABLET APPS</h2>
    <p class="feature-text">This is a simple hero unit, a simple jumbotron- style component for calling extra attention to featured content.</p>
    <div class="feature-btn">LEARN MORE</div>
  </article>
  <article class="feature" style="left:104px;top:775px">
    <div class="feature-icon" role="img" aria-label="Analytics chart icon" style="background:linear-gradient(#d9423a 0 30%,#62b0e8 30%,#1f63c4)"></div>
    <h2 class="feature-band">REAL-TIME ANALYTICS</h2>
    <p class="feature-text">This is a simple hero unit, a simple jumbotron- style component for calling extra attention to featured content.</p>
    <div class="feature-btn">LEARN MORE</div>
  </article>
  <article class="feature" style="left:365px;top:775px">
    <div class="feature-icon" role="img" aria-label="Connected people network icon" style="background:linear-gradient(135deg,#e34b3b,#f2c32c,#41a940,#2e77d0)"></div>
    <h2 class="feature-band">SOCIAL NETWORK INTEGRATION</h2>
    <p class="feature-text">This is a simple hero unit, a simple jumbotron- style component for calling extra attention to featured content.</p>
    <div class="feature-btn">LEARN MORE</div>
  </article>
  <article class="feature" style="left:626px;top:775px">
    <div class="feature-icon" role="img" aria-label="Dollar coin icon" style="border-radius:50%;background:radial-gradient(#a9cbec,#6f9fd0)"></div>
    <h2 class="feature-band">ENHANCED SPONSORSHIP OPPORTUNITIES</h2>
    <p class="feature-text">This is a simple hero unit, a simple jumbotron- style component for calling extra attention to featured content.</p>
    <div class="feature-btn">LEARN MORE</div>
  </article>
</main>

<footer class="site-footer">
  <nav class="footer-nav">
    <span style="left:122px">ABOUT</span><span style="left:178px">FEATURES</span><span style="left:251px">FAQ</span>
    <span style="left:297px">BLOG</span><span style="left:352px">PRESS</span><span style="left:409px">REGISTER</span><span style="left:476px">LOGIN</span>
  </nav>
  <div class="contact" style="left:122px">
    <svg width="19" height="13" viewBox="0 0 19 13"><rect x=".5" y=".5" width="18" height="12" fill="#eee" stroke="#bbb"/><path d="M1 1l8.5 6L18 1" fill="none" stroke="#aaa"/></svg>
    help@corvana.com
  </div>
  <div class="contact" style="left:246px">
    <svg width="16" height="16" viewBox="0 0 16 16"><path d="M3 1l3 3-2 2c1 2 4 5 6 6l2-2 3 3-2 2C8 15 1 8 1 3z" fill="#bbb"/></svg>
    +00 (0) 000 000
  </div>
  <p class="copyright">© Copyright 2013 Corvana. All Rights Reserved</p>
  <h3 class="newsletter-title">Join our Newsletter</h3>
  <div class="newsletter-input">Please your enter email id</div>
  <div class="newsletter-send">SEND</div>
  <p class="follow">Corvana on</p>
  <span class="social-foot" style="left:654px"></span>
  <span class="social-foot" style="left:680px"></span>
  <span class="social-foot" style="left:706px"></span>
  <span class="social-foot" style="left:733px"></span>
  <span class="social-foot" style="left:760px"></span>
</footer>

</body>
</html>
```